Quarvine, Cosmetic skin care line

I am not looking to change my logo quarvine on the label just want someone to design a different label I want it to be very classy as it is already just want something different. My product target classier people and people with higher income and for woman and men but mostly women. Looking to keep the label background black

Target Market(s)

Classier and higer income women/men mostly women

Industry/Entity Type

Cosmetics

• I don't really know

Colors

Designer to choose colors to be used in the design.

Requirements
Must have
• It must keep the same quarvine logo and the same matte black background color
Nice to have
• I want a different layout and maybe different fonts for the label
Should not have

```html
<!DOCTYPE html>
<html lang="en">
<head>
<meta charset="utf-8">
<title>Quarvine Eye Corrector Serum Label</title>
<link rel="stylesheet" href="https://fonts.googleapis.com/css2?family=Poppins:wght@300;400&family=Playfair+Display:wght@700&family=Playfair+Display:ital,wght@1,400&display=swap">
<style>
  :root {
    --page: #ffffff;
    --frame-line: #dcdcdc;
    --label-black: #000000;
    --ink-light: #ffffff;
    --ink-dark: #333333;
  }
  * { margin: 0; padding: 0; box-sizing: border-box; }
  html, body {
    width: 1200px;
    height: 1119px;
    overflow: hidden;
    background: var(--page);
  }
  .canvas {
    position: relative;
    width: 1200px;
    height: 1119px;
    background: var(--page);
  }
  .canvas-frame {
    position: absolute;
    inset: 2px;
    border: 1px solid var(--frame-line);
  }
  .label {
    position: absolute;
    left: 221px;
    top: 232px;
    width: 718px;
    height: 643px;
    background: var(--label-black);
    color: var(--ink-light);
  }
  .brand-name {
    position: absolute;
    left: 0;
    width: 100%;
    top: 330px;
    top: 98px;
    text-align: center;
    font-family: "Poppins", sans-serif;
    font-weight: 300;
    font-size: 66px;
    line-height: 1;
    letter-spacing: 0.14em;
    padding-left: 0.14em;
  }
  .trademark {
    position: absolute;
    left: 548px;
    top: 201px;
    font-family: "Poppins", sans-serif;
    font-weight: 400;
    font-size: 15px;
    line-height: 1;
  }
  .tagline {
    position: absolute;
    left: 0;
    width: 100%;
    top: 210px;
    text-align: center;
    font-family: "Playfair Display", serif;
    font-style: italic;
    font-weight: 400;
    font-size: 40px;
    line-height: 1;
  }
  .product-band {
    position: absolute;
    left: 0;
    top: 347px;
    width: 100%;
    height: 70px;
    background: var(--ink-light);
    color: var(--ink-dark);
    display: flex;
    align-items: center;
    justify-content: center;
    font-family: "Poppins", sans-serif;
    font-weight: 400;
    font-size: 43px;
    letter-spacing: 0.01em;
  }
  .product-type {
    position: absolute;
    left: 0;
    width: 100%;
    top: 497px;
    text-align: center;
    font-family: "Playfair Display", serif;
    font-weight: 700;
    font-size: 49px;
    line-height: 1;
  }
  .product-detail {
    position: absolute;
    left: 0;
    width: 100%;
    top: 562px;
    text-align: center;
    font-family: "Poppins", sans-serif;
    font-weight: 400;
    font-size: 20px;
    line-height: 1;
  }
  .accent-rule {
    position: absolute;
    left: 297px;
    top: 597px;
    width: 125px;
    height: 10px;
    background: var(--ink-light);
  }
</style>
</head>
<body>
  <div class="canvas">
    <div class="canvas-frame"></div>
    <section class="label">
      <div class="brand-name">QUARVINE</div>
      <div class="trademark">™</div>
      <div class="tagline">for all</div>
      <div class="product-band">EYE CORRECTOR</div>
      <div class="product-type">Serum</div>
      <div class="product-detail">WITH TRIPE PEPTIDES</div>
      <div class="accent-rule"></div>
    </section>
  </div>
</body>
</html>
```